Stationery Design Project

Fire and building compliance company needs business card, letterhead and complement slip designed.
Have included a brief about business card, basic want front keep quite clean with just the KTW logo and the words Marloway Alarm and Safety 2012 Ltd (small print) along the bottom. Website needs to be included (www.ktwalarm.example.nz) on either front or back.
The info for back is as per attachment.
Letterhead and complement slip should have the usual stuff KTW logo etc and also the accredited test lab logo at the bottom (can be small size)
Target Market(s)
Property owners, buisness managers
Industry/Entity Type
Building
Look and feel
Each slider illustrates characteristics of the customer's brand and the style your logo design should communicate.

```html
<!DOCTYPE html>
<html lang="en">
<head>
<meta charset="utf-8">
<title>KTW Business Card</title>
<link href="https://fonts.googleapis.com/css2?family=Open+Sans:wght@400;600;700&display=swap" rel="stylesheet">
<style>
  :root {
    --backdrop: #e9e6e1;
    --blue-dark: #0b5a86;
    --blue: #1577a8;
    --blue-light: #2d92c4;
    --orange: #f39323;
    --orange-deep: #e8701a;
    --white: #ffffff;
    --ink: #3a3a3a;
    --navy: #1c2a5a;
  }
  * { margin: 0; padding: 0; box-sizing: border-box; }
  html, body {
    width: 1200px; height: 900px; overflow: hidden;
    background: var(--backdrop);
    font-family: "Open Sans", sans-serif;
  }
  .sheet { position: relative; width: 1200px; height: 900px; }
  .card {
    position: absolute; left: 250px; width: 700px; height: 400px;
    overflow: hidden; box-shadow: 0 6px 18px rgba(0,0,0,0.18);
  }
  /* Back: services */
  .card-back {
    top: 40px;
    background: linear-gradient(135deg, var(--blue-light) 0%, var(--blue) 45%, var(--blue-dark) 100%);
    color: var(--white); text-align: center;
  }
  .brand { display: inline-flex; align-items: center; gap: 12px; }
  .brand-dot { width: 34px; height: 34px; border-radius: 50%; }
  .brand-name { font-weight: 700; font-size: 44px; letter-spacing: 1px; line-height: 1; }
  .card-back .brand { margin-top: 62px; }
  .card-back .brand-dot { background: var(--white); }
  .services-title { margin-top: 30px; font-weight: 700; font-size: 19px; }
  .services-list { list-style: none; margin-top: 4px; font-size: 17px; line-height: 1.4; }
  .services-list li::before {
    content: ""; display: inline-block; width: 7px; height: 7px;
    border: 1.5px solid var(--white); border-radius: 50%;
    margin-right: 8px; vertical-align: middle;
  }
  /* Front: contact */
  .card-front { top: 470px; background: var(--white); }
  .front-art { position: absolute; inset: 0; }
  .card-front .brand { position: absolute; left: 50px; top: 80px; color: var(--ink); }
  .card-front .brand-dot { background: var(--orange); }
  .lab-badge {
    position: absolute; left: 52px; top: 270px; width: 62px; height: 62px;
    background: var(--navy); border-radius: 6px;
  }
  .contact { position: absolute; left: 470px; top: 168px; width: 222px; color: var(--white); }
  .person-name { font-weight: 700; font-size: 18px; line-height: 1.3; }
  .person-role { font-size: 14px; margin-bottom: 10px; }
  .contact-row { display: flex; align-items: flex-start; gap: 9px; font-size: 14px; line-height: 1.3; margin-bottom: 4px; }
  .contact-row strong { font-weight: 700; }
  .icon { flex: 0 0 17px; width: 17px; height: 17px; margin-top: 1px; }
  .contact-web { margin-top: 4px; font-size: 14px; padding-left: 26px; }
</style>
</head>
<body>
<main class="sheet">

  <section class="card card-back">
    <div class="brand">
      <span class="brand-dot"></span>
      <span class="brand-name">KTW</span>
    </div>
    <h2 class="services-title">Our services</h2>
    <ul class="services-list">
      <li>Building compliance specialists</li>
      <li>Building warrant of fitness preparation</li>
      <li>Fire alarms, Fire Extinguishers &amp; emergency lighting</li>
      <li>Approved evacuation schemes</li>
      <li>Pressure testing LPG CNG Fire extinguishers</li>
      <li>Security alarm and CCTV systems</li>
    </ul>
  </section>

  <section class="card card-front">
    <svg class="front-art" width="700" height="400" viewBox="0 0 700 400" aria-hidden="true">
      <defs>
        <linearGradient id="panelBlue" x1="0" y1="0" x2="1" y2="1">
          <stop offset="0" stop-color="#2d92c4"/>
          <stop offset="1" stop-color="#0b5a86"/>
        </linearGradient>
      </defs>
      <path d="M230 400 C262 226 410 96 700 56 L700 72 C420 112 276 236 248 400 Z" fill="var(--orange)"/>
      <path d="M212 400 C240 280 320 190 420 140 C330 200 262 290 228 400 Z" fill="var(--orange-deep)"/>
      <path d="M260 400 C290 240 430 120 700 90 L700 400 Z" fill="url(#panelBlue)"/>
    </svg>

    <div class="brand">
      <span class="brand-dot"></span>
      <span class="brand-name">KTW</span>
    </div>
    <div class="lab-badge" role="img" aria-label="Accredited test laboratory badge"></div>

    <div class="contact">
      <p class="person-name">Daniel Moretti</p>
      <p class="person-role">Operator</p>
      <div class="contact-row">
        <svg class="icon" viewBox="0 0 18 18" aria-hidden="true"><circle cx="9" cy="9" r="9" fill="var(--orange)"/><path d="M9 4a3 3 0 0 0-3 3c0 2.3 3 6 3 6s3-3.7 3-6a3 3 0 0 0-3-3z" fill="#fff"/></svg>
        <span><strong>Marloway Alarm and Safety 2012 Ltd</strong><br>18 Harlow Street Extension<br>Rivermouth, 4500</span>
      </div>
      <div class="contact-row">
        <svg class="icon" viewBox="0 0 18 18" aria-hidden="true"><circle cx="9" cy="9" r="9" fill="var(--orange)"/><path d="M6 4.5l2 2-1 1.2a6 6 0 0 0 3.3 3.3l1.2-1 2 2-1.3 1.5C8.5 13.5 4.5 9.5 4.5 5.8z" fill="#fff"/></svg>
        <span>06 555 0182</span>
      </div>
      <div class="contact-row">
        <svg class="icon" viewBox="0 0 18 18" aria-hidden="true"><circle cx="9" cy="9" r="9" fill="var(--orange)"/><rect x="5" y="6" width="8" height="6" fill="#fff"/><rect x="6.5" y="4" width="5" height="2.5" fill="#fff"/></svg>
        <span>06 555 0147</span>
      </div>
      <div class="contact-row">
        <svg class="icon" viewBox="0 0 18 18" aria-hidden="true"><circle cx="9" cy="9" r="9" fill="var(--orange)"/><rect x="4.5" y="6" width="9" height="6.5" fill="#fff"/><path d="M4.5 6l4.5 3.5L13.5 6" fill="none" stroke="var(--orange)" stroke-width="1"/></svg>
        <span>admin@marloway.example.nz</span>
      </div>
      <p class="contact-web">www.ktwalarm.example.nz</p>
    </div>
  </section>

</main>
</body>
</html>
```